Letterhead design for business

Looking for an attractive and professional letterhead that uses the logo that is attached below.

Target Market(s)

Potential bankruptcy clients.

Industry/Entity Type

Legal

Colors

Designer to choose colors to be used in the design.

Requirements
Must have
• Address for locations, phone number, and website address.
• Addresses are on website ferncoveadvice.example. Use following phone number (for tracking purposes): 555-013-8274

```html
<!DOCTYPE html>
<html lang="en">
<head>
<meta charset="utf-8">
<title>Ferncove Advice Group – Letterhead</title>
<link href="https://fonts.googleapis.com/css2?family=Itim&family=Dosis:wght@500;600&display=swap" rel="stylesheet">
<style>
  :root{
    --green:#86c08a;
    --green-light:#a4d3a6;
    --charcoal:#343434;
    --slate:#6a6b6d;
    --ink:#5c5c5c;
    --text-dark:#222;
    --paper:#fbfbfd;
    --backdrop:#e9ebe8;
  }
  *{margin:0;padding:0;box-sizing:border-box}
  html,body{width:1200px;height:1200px;overflow:hidden;background:var(--backdrop)}
  .letterhead{
    position:absolute;left:185px;top:38px;width:830px;height:1124px;
    background:var(--paper);overflow:hidden;
    font-family:"Itim",cursive;color:var(--ink);
    box-shadow:0 2px 10px rgba(0,0,0,.12);
  }
  .corner-accent{position:absolute;left:0;top:0}
  .headline{position:absolute;left:128px;top:196px;font-size:31px;color:var(--green);font-weight:400;letter-spacing:.5px}
  .body-copy{position:absolute;left:128px;width:545px;font-size:15px;line-height:20.4px}
  .copy-intro{top:260px}
  .copy-main{top:377px;left:130px}
  .copy-close{top:662px;left:130px}
  .doc-label{position:absolute;left:605px;top:718px;text-align:center;color:var(--slate)}
  .doc-label .title{font-size:22px;border-bottom:2px solid var(--slate);line-height:24px;padding:0 2px}
  .doc-label .date{font-size:16px;letter-spacing:1px}
  .contact-list{position:absolute;left:160px;top:800px;list-style:none}
  .contact-list li{display:flex;align-items:flex-start;height:54px;color:var(--text-dark);font-family:"Dosis",sans-serif;font-weight:600}
  .contact-list svg{width:26px;height:26px;flex:none;margin-right:18px}
  .contact-list .phone{font-size:17px;letter-spacing:1.5px;font-weight:500}
  .contact-list .web{font-size:14px}
  .contact-list .address{font-size:12.5px;line-height:16px}
  .contact-list .address span{display:block;text-align:center}
  .brand{position:absolute;left:585px;top:950px;width:250px;text-align:center}
  .brand-mark{width:16px;height:16px;background:var(--green);border-radius:50%;margin:0 auto 12px}
  .brand-name{font-family:"Dosis",sans-serif;font-weight:600;font-size:25px;color:var(--green);line-height:30px;white-space:nowrap}
  .brand-sub{font-family:"Dosis",sans-serif;font-weight:500;font-size:15px;color:var(--green);line-height:20px;margin-top:6px;white-space:nowrap}
  .base-band{position:absolute;left:0;bottom:0}
</style>
</head>
<body>
<main class="letterhead">
  <svg class="corner-accent" width="210" height="206" viewBox="0 0 210 206" aria-hidden="true">
    <polygon points="0,0 210,0 0,206" fill="var(--charcoal)"/>
    <polygon points="118,0 210,0 70,138 45,110" fill="var(--slate)"/>
    <polygon points="0,0 122,0 0,118" fill="var(--green)"/>
    <polygon points="0,0 122,0 60,58" fill="var(--green-light)"/>
  </svg>

  <h1 class="headline">HEADLINE</h1>

  <p class="body-copy copy-intro">We are a Georgia Law Firm dedicated to being a valuable resource for all of the debt woes that ordinary people face. We are experienced bankruptcy attorneys with litigation experience that understand that people need more than just your typical bankruptcy lawyer. People need someone that is experienc</p>

  <p class="body-copy copy-main">We are a Georgia Law Firm dedicated to being a valuable resource for all of the debt woes that ordinary people face. We are experienced bankruptcy attor­neys with litigation experience that understand that people need more than just your typical bankruptcy lawyer. People need someone that is experienced in handling all of the practical aspects of avoiding bankruptcy, recovering from bankruptcy quickly, tackling stubborn student loans, and punishing abusive debt collectors in court when they violate the law. Let us help you navigate your options and find a solution for your troubling debt.We are a Georgia Law Firm dedicatelaw. Let us help you navigate your options and find a solution for your troubling debt.Georgia Law Firm dedicatelaw. Let us help you navigate your options and find a solution for your troubling debt.</p>

  <p class="body-copy copy-close">We are a Georgia Law Firm dedicated to being a valuable resource for all of the debt woes that ordinary people face.</p>

  <div class="doc-label">
    <div class="title">letterhead</div>
    <div class="date">11.05.2018</div>
  </div>

  <ul class="contact-list">
    <li class="phone">
      <svg viewBox="0 0 24 24" aria-hidden="true"><path d="M6.6 2.5l3 3.4-1.8 2.4c1.3 3 3.6 5.4 6.5 6.8l2.4-1.8 3.4 3-1.6 3.2C11 19 4.8 12.6 3.5 4.1z" fill="var(--green)"/></svg>
      555-013-8274
    </li>
    <li class="web">
      <svg viewBox="0 0 24 24" aria-hidden="true"><path d="M2 10l10-7 10 7v11H2z" fill="var(--green)"/><path d="M2 10l10 6 10-6" fill="none" stroke="#fff" stroke-width="1.5"/></svg>
      https://ferncoveadvice.example/
    </li>
    <li class="address">
      <svg viewBox="0 0 24 24" aria-hidden="true"><path d="M2 9l5-2 5 2 5-2v14l-5 2-5-2-5 2z" fill="none" stroke="var(--green)" stroke-width="1.5"/><circle cx="17" cy="6" r="3.5" fill="none" stroke="var(--green)" stroke-width="1.5"/><path d="M17 9.5v4" stroke="var(--green)" stroke-width="1.5"/></svg>
      <div><span>48 Alder Row, Suite #310 Brookhaven,</span><span>Georgia 30999</span></div>
    </li>
  </ul>

  <div class="brand">
    <div class="brand-mark"></div>
    <div class="brand-name">Ferncove Advice Group</div>
    <div class="brand-sub">by Attorney M. Larkspur</div>
  </div>

  <svg class="base-band" width="830" height="49" viewBox="0 0 830 49" aria-hidden="true">
    <path d="M0 0H584C592 0 596 5 600 14L610 30C613 35 616 36 622 36H830V49H0Z" fill="var(--green)"/>
  </svg>
</main>
</body>
</html>
```